Used Car Dealer seeks an Amazing Business Card Design

We are looking for a business card design that incorporates our logo and grabs the attention of anyone we give the business card to.

Looking to use the same colors as the logo. Our Logo choice is the black background with Red and Silver/Grey Lettering.

We also would like to see some embossed designs.

Target Market(s)

Used Car Buyers, Automotive, Auto

Industry/Entity Type

Automotive

Contact Information for Business Card

BVEL7K
Gordon Whitlock
482 Tarrow Lane
Suite 207
Ashvale, QX 00512
Office (555) 555-0142
Cell (555) 555-0187
bvel7kga@quellmail.com
www.bvel7kga.com

Colors
ffffff
ee3036

Requirements
Must have
• Must include our logo (Black Background with Red and Silver/Grey Lettering)
Nice to have
• Embossed Design. Can be Single or Double Sided.

```html
<!DOCTYPE html>
<html lang="en">
<head>
<meta charset="utf-8">
<title>BVEL7K – Gordon Whitlock Business Card</title>
<link rel="stylesheet" href="https://fonts.googleapis.com/css2?family=Open+Sans:wght@400;700&display=swap">
<style>
  :root {
    --navy: #111726;
    --paper: #f4f5f5;
    --red: #ee2a3c;
    --red-fold: #c8102e;
    --amber: #f6ab3b;
    --ink: #15192a;
    --silver: #c6c9ce;
    --white: #ffffff;
  }
  html, body {
    margin: 0;
    padding: 0;
    width: 1200px;
    height: 700px;
    overflow: hidden;
    background: var(--paper);
  }
  .card {
    position: relative;
    width: 1200px;
    height: 700px;
    overflow: hidden;
    background: var(--paper);
    font-family: "Open Sans", Arial, sans-serif;
    color: var(--ink);
  }
  .card-backdrop {
    position: absolute;
    inset: 0;
  }
  .brand-name {
    position: absolute;
    left: 60px;
    top: 330px;
    width: 440px;
    text-align: center;
    margin: 0;
    font-size: 104px;
    font-weight: 700;
    line-height: 1;
    letter-spacing: 1px;
    color: var(--silver);
  }
  .name-band {
    position: absolute;
    left: 637px;
    top: 63px;
    width: 513px;
    height: 97px;
    background: var(--red);
    display: flex;
    align-items: center;
  }
  .person-name {
    margin: 0 0 0 100px;
    font-size: 45px;
    font-weight: 700;
    color: var(--white);
    white-space: nowrap;
  }
  .job-title {
    position: absolute;
    left: 805px;
    top: 164px;
    margin: 0;
    font-size: 38px;
    font-weight: 400;
    letter-spacing: 7px;
    color: var(--ink);
  }
  .contact-list {
    list-style: none;
    margin: 0;
    padding: 0;
  }
  .contact-item {
    position: absolute;
    left: 697px;
    display: flex;
    align-items: center;
    transform: translateY(-50%);
  }
  .contact-icon {
    width: 48px;
    height: 48px;
    flex: none;
  }
  .contact-text {
    margin-left: 42px;
    font-size: 31px;
    line-height: 37px;
    letter-spacing: 0.4px;
    color: var(--ink);
    white-space: nowrap;
  }
  .contact-item--office { top: 327px; }
  .contact-item--cell { top: 393px; }
  .contact-item--address { top: 481px; }
  .contact-item--web { top: 574px; }
  .contact-item--web .contact-text { margin-left: 45px; }
  .contact-item--email { top: 641px; }
  .contact-item--email .contact-text { letter-spacing: 0; }
</style>
</head>
<body>
<main class="card">
  <svg class="card-backdrop" width="1200" height="700" viewBox="0 0 1200 700" aria-hidden="true">
    <polygon points="0,0 815,0 522,700 0,700" fill="var(--navy)"/>
    <polygon points="637,160 748,160 714,240" fill="var(--red-fold)"/>
  </svg>

  <p class="brand-name">BVEL7K</p>

  <div class="name-band">
    <h1 class="person-name">Gordon Whitlock</h1>
  </div>
  <p class="job-title">Manager</p>

  <ul class="contact-list">
    <li class="contact-item contact-item--office">
      <svg class="contact-icon" viewBox="0 0 48 48" aria-label="Office phone">
        <circle cx="24" cy="24" r="24" fill="var(--amber)"/>
        <path d="M16 13c1.5-1 3-1 4 .5l2.5 4c.6 1 .3 2.2-.6 2.9l-1.6 1.2c1.2 2.6 3.4 4.8 6 6l1.2-1.6c.7-.9 1.9-1.2 2.9-.6l4 2.5c1.5 1 1.5 2.5.5 4l-1.5 2c-1.2 1.6-3.8 1.8-6.2.7-6.3-2.8-11-7.5-13.8-13.8-1.1-2.4-.9-5 .7-6.2z" fill="var(--white)"/>
      </svg>
      <span class="contact-text">(555) 555-0142</span>
    </li>
    <li class="contact-item contact-item--cell">
      <svg class="contact-icon" viewBox="0 0 48 48" aria-label="Cell phone">
        <circle cx="24" cy="24" r="24" fill="var(--amber)"/>
        <rect x="17" y="12" width="14" height="25" rx="3" fill="var(--white)"/>
        <rect x="19.5" y="15.5" width="9" height="8" fill="var(--amber)"/>
        <rect x="19" y="7" width="2" height="6" fill="var(--white)"/>
        <circle cx="24" cy="31" r="2" fill="var(--amber)"/>
      </svg>
      <span class="contact-text">(555) 555-0187</span>
    </li>
    <li class="contact-item contact-item--address">
      <svg class="contact-icon" viewBox="0 0 48 48" aria-label="Address">
        <circle cx="24" cy="24" r="24" fill="var(--amber)"/>
        <path d="M12 20l3-7h18l3 7z" fill="var(--white)"/>
        <rect x="13" y="21" width="22" height="15" fill="none" stroke="var(--white)" stroke-width="2.5"/>
        <rect x="19" y="26" width="10" height="10" fill="none" stroke="var(--white)" stroke-width="2.5"/>
      </svg>
      <span class="contact-text">482 Tarrow Lane<br>Suite 207<br>Ashvale, QX 00512</span>
    </li>
    <li class="contact-item contact-item--web">
      <svg class="contact-icon" viewBox="0 0 48 48" aria-label="Website">
        <circle cx="24" cy="24" r="24" fill="var(--amber)"/>
        <circle cx="24" cy="24" r="14" fill="none" stroke="var(--white)" stroke-width="2.5"/>
        <path d="M14 18l10 3 8-7M21 21l-3 14M24 21l10 10" fill="none" stroke="var(--white)" stroke-width="2.5"/>
        <circle cx="24" cy="21" r="3" fill="var(--white)"/>
        <circle cx="18" cy="35" r="2.5" fill="var(--white)"/>
        <circle cx="34" cy="31" r="2.5" fill="var(--white)"/>
      </svg>
      <span class="contact-text">www.bvel7kga.com</span>
    </li>
    <li class="contact-item contact-item--email">
      <svg class="contact-icon" viewBox="0 0 48 48" aria-label="Email">
        <circle cx="24" cy="24" r="24" fill="var(--amber)"/>
        <rect x="12" y="15" width="24" height="18" rx="1.5" fill="var(--white)"/>
        <path d="M12.5 16l11.5 10 11.5-10M12.5 32.5l9-8M35.5 32.5l-9-8" fill="none" stroke="var(--amber)" stroke-width="1.8"/>
      </svg>
      <span class="contact-text">bvel7kga@quellmail.com</span>
    </li>
  </ul>
</main>
</body>
</html>
```